I need a business card design for a new company that will be doing consulting work around issues of cultural competency, and diversity and inclusion. I would like the design to be crisp and clear with bold but conservative colors and incorporate shades of blue

Target Market(s)

Small businesses, schools, non-profits

Industry/Entity Type

Consulting

Font styles to use
Serif
Sans Serif

Colors
0c5ba6
6b449b
3276b5
0292cd

Requirements
Must have
• A Morrow Venture (name of company)
• Tiru Morrow
• CEO
• tiru@amorrowventure.example
• (215)555-0147

```html
<!DOCTYPE html>
<html lang="en">
<head>
<meta charset="utf-8">
<title>Tiru Morrow – Business Card</title>
<link rel="stylesheet" href="https://fonts.googleapis.com/css2?family=Arimo:wght@400;700&display=swap">
<style>
  :root {
    --paper: #ffffff;
    --trim: #000000;
    --cyan: #00ffff;
    --sky: #1ec8ff;
    --azure: #3a7dff;
    --header-blue: #0f4ff5;
    --contact-violet: #4a25ff;
    --text-light: #ffffff;
    --icon-red: #e8141b;
  }
  * { margin: 0; padding: 0; box-sizing: border-box; }
  html, body {
    width: 1200px; height: 841px; overflow: hidden;
    background: var(--paper);
    font-family: "Arimo", Arial, sans-serif;
  }
  .sheet { position: relative; width: 1200px; height: 841px; }

  .crop-mark { position: absolute; background: var(--trim); }
  .crop-mark.vertical { width: 1px; height: 120px; }
  .crop-mark.horizontal { height: 1px; width: 120px; }

  .card {
    position: absolute; left: 152px; top: 152px;
    width: 896px; height: 536px; overflow: hidden;
  }
  .card-front {
    position: absolute; left: 0; top: 0; width: 896px; height: 336px;
    background: linear-gradient(120deg,
      var(--sky) 0%, var(--azure) 14%, var(--cyan) 30%, var(--azure) 50%,
      var(--cyan) 68%, var(--azure) 84%, var(--sky) 100%);
  }
  .header-shape { position: absolute; left: 0; top: 0; }
  .identity {
    position: absolute; left: 404px; top: 62px; color: var(--text-light);
  }
  .person-name { font-weight: 700; font-size: 57px; line-height: 1; letter-spacing: 0.5px; }
  .person-role { font-weight: 400; font-size: 30px; line-height: 1; margin-top: 10px; }

  .contact-band {
    position: absolute; left: 0; top: 336px; width: 896px; height: 200px;
    background: var(--contact-violet);
  }
  .contact-line {
    position: absolute; left: 38px; display: flex; align-items: center; gap: 10px;
    color: var(--text-light); font-weight: 700; font-size: 38px;
  }
  .contact-line.email { top: 30px; }
  .contact-line.phone { top: 98px; }
  .contact-icon { width: 46px; height: 46px; flex: none; }
</style>
</head>
<body>
<div class="sheet">
  <span class="crop-mark vertical" style="left:179px;top:0"></span>
  <span class="crop-mark vertical" style="left:1020px;top:0"></span>
  <span class="crop-mark vertical" style="left:179px;top:721px"></span>
  <span class="crop-mark vertical" style="left:1020px;top:721px"></span>
  <span class="crop-mark horizontal" style="left:0;top:179px"></span>
  <span class="crop-mark horizontal" style="left:0;top:661px"></span>
  <span class="crop-mark horizontal" style="left:1080px;top:179px"></span>
  <span class="crop-mark horizontal" style="left:1080px;top:661px"></span>

  <div class="card">
    <div class="card-front">
      <svg class="header-shape" width="896" height="336" viewBox="0 0 896 336">
        <path d="M231 0 H896 V209 H400 C300 209 238 130 231 0 Z" fill="var(--header-blue)"/>
      </svg>
      <div class="identity">
        <h1 class="person-name">Tiru Morrow</h1>
        <p class="person-role">CEO - A Morrow Venture</p>
      </div>
    </div>

    <div class="contact-band">
      <div class="contact-line email">
        <svg class="contact-icon" viewBox="0 0 46 46" aria-hidden="true">
          <rect x="2" y="2" width="42" height="42" rx="8" fill="none" stroke="#fff" stroke-width="3"/>
          <path d="M15 11 l5 -1 3 7 -3 3 c2 4 4 6 7 8 l3 -3 7 3 -1 5 c-12 1 -22 -10 -21 -22 z" fill="#fff"/>
        </svg>
        <span>tiru@amorrowventure.example</span>
      </div>
      <div class="contact-line phone">
        <svg class="contact-icon" viewBox="0 0 46 46" aria-hidden="true">
          <rect x="2" y="2" width="42" height="42" rx="8" fill="none" stroke="#fff" stroke-width="3"/>
          <rect x="9" y="13" width="28" height="20" fill="var(--icon-red)"/>
          <path d="M9 13 L23 25 L37 13 M9 33 L19 22 M37 33 L27 22" fill="none" stroke="#fff" stroke-width="2"/>
        </svg>
        <span>(215)555-0147</span>
      </div>
    </div>
  </div>
</div>
</body>
</html>
```